Packaging / Logo Design for Toddler Potty Liners

We need a packaging and logo design for a new company based in Atlanta called "WeeMeadow". We manufacture innovative, eco-friendly baby / toddler products. Our initial product is a flushable, biodegradable potty liner used for toddler potty training. We are looking for a modern / clean / eco-friendly packaging and logo design for this product. Each package will contain 20 liners. Box dimensions are as follows:

Length = 8.5in
Width = 5in
Height = 1.5in

The box will have a perforated top measuring 6.5 inches (see attached pictures). Liners will be folded inside and individually pulled out through the perforated top (similar to a Softrel box). See attached pictures of similar box.

Packaging should appeal to parents as an easy to use, eco-friendly, sanitary solution to potty training. This product is an alternative to the conventional way of cleaning / disinfecting the potty after each use, a process that most parents dread!

The closest competitors are NeatNips (www.neatnips-example.com) and Brillo (www.brillo-example.com) - you can reference their websites to get an idea for the product and use. However, their liners are not flushable and that is the biggest differentiator of this product. Their packaging seems conventional and non-inspiring so we would like our design to stand out from theirs.

We would like to see creative, modern cardboard box designs which will make our brand stand out from the competition. We would like to use one of the following color schemes: 1) a modern green color on a white background, 2) a modern green color on plain cardboard background, or 3) white on a modern green background. May use one or two additional complementary colors. See attached modern green image for inspiration. We would like to see clean lines, text and illustrations. We are looking forward to seeing any cool ideas you may have!
Updates

Brief has been updated with our desired color schemes and pictures for inspiration.  Please read updated brief before beginning your design!  Thanks so much!

Industry/Entity Type

Biodegradable

Requirements
Must have
• The front of the package should include the following info:

Logo: WeeMeadow
Product Name: Flushable Potty Chair Liners
Clean and Convenient
Fits All Potty Chairs
Sewer and Septic Safe
Patent Pending
20 Single-Use Flushable Potty Chair Liners

Package should also have space for some simple instructions (preferably with illustrations). This can be placed on one of the sides of the box.
1. Place liner over clean, dry (underline the word dry) potty bowl.
2. After your toddler uses the potty, remove liner (do not tie) and flush.
3. Give your toddler a high five!

Please submit design considering all sides of the box!

```html
<!DOCTYPE html>
<html lang="en">
<head>
<meta charset="UTF-8">
<title>WeeMeadow Flushable Potty Chair Liners – Box Panels</title>
<link href="https://fonts.googleapis.com/css2?family=Comfortaa:wght@400;700&family=Sniglet:wght@400;800&family=Kaushan+Script&display=swap" rel="stylesheet">
<style>
  :root {
    --stage: #e6e6e6;
    --card: #cdbb9c;
    --card-dark: #b9a684;
    --green: #5f9a5b;
    --green-deep: #4c8750;
    --green-soft: #9cc08e;
    --orange: #f39325;
    --cream: #f3ede2;
    --ink: #ffffff;
    --label: #222222;
  }
  * { box-sizing: border-box; margin: 0; padding: 0; }
  html, body { width: 1200px; height: 900px; overflow: hidden; }
  body {
    background: var(--stage);
    font-family: "Comfortaa", sans-serif;
  }
  .box-net {
    position: absolute;
    left: 140px; top: 110px;
    display: flex;
    height: 620px;
    box-shadow: 0 10px 30px rgba(0,0,0,.12);
  }
  .panel {
    position: relative;
    height: 100%;
    background: var(--card);
    overflow: hidden;
  }
  .panel--side { width: 110px; background: var(--card-dark); }
  .panel--face { width: 350px; }
  .panel + .panel { border-left: 1px solid rgba(0,0,0,.08); }

  .meadow {
    position: absolute; left: 0; right: 0; bottom: 0;
    height: 270px;
    background: linear-gradient(to bottom, rgba(156,192,142,0) 0%, var(--green-soft) 38%, var(--green) 66%, var(--green-deep) 100%);
  }

  .brand {
    font-family: "Comfortaa", sans-serif;
    font-weight: 700;
    color: var(--green);
    font-size: 30px;
    text-align: center;
    letter-spacing: -0.5px;
  }
  .product-title {
    font-family: "Sniglet", sans-serif;
    font-weight: 800;
    color: var(--orange);
    font-size: 30px;
    line-height: 1.05;
    text-align: center;
    transform: rotate(-6deg);
  }

  /* front */
  .front .brand { margin-top: 42px; }
  .front .product-title { margin-top: 22px; }
  .features {
    list-style: none;
    position: absolute; left: 28px; top: 258px;
    color: var(--ink);
    font-size: 14px;
    line-height: 1.65;
  }
  .features li::before {
    content: "";
    display: inline-block;
    width: 6px; height: 6px;
    border-radius: 50%;
    background: var(--orange);
    margin-right: 7px;
    vertical-align: middle;
  }
  .eco-seal {
    position: absolute;
    text-align: center;
  }
  .eco-seal__ring {
    width: 62px; height: 62px;
    border-radius: 50%;
    border: 4px solid var(--green);
    background: var(--cream);
    margin: 0 auto;
  }
  .eco-seal__caption {
    font-family: "Kaushan Script", cursive;
    color: var(--ink);
    font-size: 14px;
    margin-top: 4px;
  }
  .front .eco-seal { right: 22px; top: 262px; }
  .count-badge {
    position: absolute; left: 18px; bottom: 26px;
    width: 46px; height: 46px;
    border-radius: 50%;
    background: var(--orange);
    color: var(--ink);
    text-align: center;
    font-family: "Sniglet", sans-serif;
    font-weight: 800;
    font-size: 18px;
    line-height: 1;
    padding-top: 9px;
  }
  .count-badge small { display: block; font-size: 7px; font-weight: 400; }

  /* back */
  .back .brand { margin-top: 42px; font-size: 26px; }
  .back .product-title { font-size: 22px; margin-top: 16px; }
  .back-copy {
    position: absolute; left: 24px; right: 24px; top: 210px;
    color: var(--ink);
    font-size: 10px;
    line-height: 1.55;
  }
  .contact {
    position: absolute; left: 24px; top: 330px;
    color: var(--ink);
    font-size: 7.5px;
    line-height: 1.7;
  }
  .back .eco-seal { right: 22px; top: 318px; }

  /* side 1 */
  .instructions { padding: 26px 10px 0; color: var(--ink); }
  .instructions__title {
    font-size: 13px;
    letter-spacing: .5px;
    margin-bottom: 12px;
  }
  .step { position: relative; margin-bottom: 12px; }
  .step__art {
    height: 62px;
    border-radius: 8px;
    background: var(--cream);
    opacity: .85;
  }
  .step__num {
    position: absolute; left: -2px; top: 48px;
    width: 20px; height: 20px;
    border-radius: 50%;
    background: var(--orange);
    color: var(--ink);
    font-family: "Sniglet", sans-serif;
    font-size: 12px;
    text-align: center;
    line-height: 20px;
  }
  .step__text { font-size: 7px; line-height: 1.35; margin-top: 10px; }
  .step__text u { text-decoration-color: var(--orange); }

  /* side 2 */
  .care-label {
    position: absolute; left: 16px; right: 16px; top: 24px;
    height: 330px;
    border-radius: 8px;
    background: var(--cream);
    border: 2px solid rgba(255,255,255,.6);
    display: flex; align-items: center; justify-content: center;
  }
  .care-label p {
    writing-mode: vertical-rl;
    font-size: 8.5px;
    line-height: 1.6;
    color: var(--green-deep);
    height: 310px;
  }

  .panel-labels {
    position: absolute; left: 140px; top: 744px;
    display: flex;
    font-family: Arial, sans-serif;
    font-size: 15px;
    color: var(--label);
  }
  .panel-labels span { text-align: center; }
  .panel-labels .side { width: 110px; }
  .panel-labels .face { width: 350px; }
</style>
</head>
<body>
  <div class="box-net">
    <section class="panel panel--side instructions-side">
      <div class="instructions">
        <h2 class="instructions__title">instructions</h2>
        <div class="step">
          <div class="step__art" role="img" aria-label="Illustration of a liner placed over a potty bowl"></div>
          <span class="step__num">1</span>
          <p class="step__text">Place liner over clean, <u>dry</u> potty bowl.</p>
        </div>
        <div class="step">
          <div class="step__art" role="img" aria-label="Illustration of a used liner being lifted out and flushed"></div>
          <span class="step__num">2</span>
          <p class="step__text">After your toddler uses the potty, remove liner (do not tie) and flush.</p>
        </div>
        <div class="step">
          <div class="step__art" role="img" aria-label="Illustration of a parent and toddler giving a high five"></div>
          <span class="step__num">3</span>
          <p class="step__text">Give your toddler a high five!</p>
        </div>
      </div>
      <div class="meadow" role="img" aria-label="Row of stylised green trees on a grassy meadow"></div>
    </section>

    <section class="panel panel--face front">
      <h1 class="brand">WeeMeadow</h1>
      <p class="product-title">Flushable Potty<br>Chair Liners</p>
      <ul class="features">
        <li>single use</li>
        <li>fits all potty chairs</li>
        <li>sewer and septic safe</li>
        <li>patent pending</li>
      </ul>
      <div class="eco-seal">
        <div class="eco-seal__ring"></div>
        <p class="eco-seal__caption">Biodegradable</p>
      </div>
      <div class="meadow" role="img" aria-label="Row of stylised green trees on a grassy meadow"></div>
      <div class="count-badge">20<small>liners</small></div>
    </section>

    <section class="panel panel--face back">
      <h2 class="brand">WeeMeadow</h2>
      <p class="product-title">Flushable Potty<br>Chair Liners</p>
      <p class="back-copy">Potty training made simple. Lay a liner over the clean bowl, let your toddler go, then lift it out and flush it away. Made from plant fibres that break down in water, each liner is gentle on pipes, septic tanks and the planet.</p>
      <address class="contact" style="font-style:normal">
        WeeMeadow Inc.<br>
        1480 Meadow Lane, Atlanta, GA<br>
        phone: (404) 555 0142 · fax: (404) 555 0143<br>
        www.weemeadow-example.com
      </address>
      <div class="eco-seal">
        <div class="eco-seal__ring"></div>
        <p class="eco-seal__caption">Biodegradable</p>
      </div>
      <div class="meadow" role="img" aria-label="Row of stylised green trees on a grassy meadow"></div>
      <div class="count-badge">20<small>liners</small></div>
    </section>

    <section class="panel panel--side care-side">
      <div class="care-label">
        <p>Each box holds twenty single-use liners. Store in a cool, dry place. Keep away from small children when not in use. Flush one liner at a time. Not for use in toilets without running water.</p>
      </div>
      <div class="meadow" role="img" aria-label="Row of stylised green trees on a grassy meadow"></div>
    </section>
  </div>

  <div class="panel-labels">
    <span class="side">side1</span>
    <span class="face">front</span>
    <span class="face">back</span>
    <span class="side">side2</span>
  </div>
</body>
</html>
```